Sunny Circle Card

4x6 Referral card double sided

basic hand drawn outline attached
not meant to be interpreted exactly but use artistic license to create what you think is best

Logo images uploaded as well

The purpose of this card is to have existing clients refer others to our office and have both of them get rewarded, however we wont put in writing that the original person gets rewarded - rather we will tell them verbally

```html
<!DOCTYPE html>
<html lang="en">
<head>
<meta charset="utf-8">
<title>Sunny Circle Referral Card</title>
<link rel="stylesheet" href="https://fonts.googleapis.com/css2?family=Tinos:wght@400;700&display=swap">
<style>
  :root {
    --stage: #e6e6e6;
    --paper: #ffffff;
    --ocean: #0a89b6;
    --ocean-deep: #0d6f97;
    --sky-line: #8dd2ea;
    --sky-top: #4f8fd6;
    --sky-mid: #b9d8ef;
    --leaf: #6db33f;
    --leaf-deep: #2f6a1f;
    --teal-ink: #137fa6;
    --shadow-blue: #0f5877;
    --white: #ffffff;
  }
  html, body {
    margin: 0;
    width: 1200px;
    height: 933px;
    overflow: hidden;
    background: var(--stage);
  }
  .card {
    position: absolute;
    left: 0;
    top: 66px;
    width: 1200px;
    height: 800px;
    background: var(--paper);
    overflow: hidden;
    font-family: "Tinos", "Times New Roman", serif;
  }
  .card-art {
    position: absolute;
    inset: 0;
    width: 1200px;
    height: 800px;
  }
  .brand {
    position: absolute;
    left: 40px;
    top: 88px;
    width: 400px;
    text-align: center;
  }
  .brand-mark {
    width: 136px;
    height: 136px;
    margin: 0 auto 36px;
    border-radius: 50%;
    background: var(--leaf);
  }
  .brand-name {
    margin: 0;
    font-weight: 400;
    font-size: 64px;
    line-height: 1;
    color: var(--teal-ink);
    letter-spacing: 1px;
  }
  .headline {
    position: absolute;
    left: 56px;
    top: 570px;
    margin: 0;
    color: var(--white);
    font-weight: 700;
    line-height: 1;
    text-shadow: 4px 4px 0 var(--shadow-blue);
  }
  .headline-top {
    display: block;
    font-size: 76px;
    letter-spacing: -1px;
  }
  .headline-top small {
    font-size: 40px;
    letter-spacing: 0;
  }
  .headline-main {
    display: block;
    margin: 8px 0 0 40px;
    font-size: 112px;
    letter-spacing: -2px;
  }
  .offer {
    position: absolute;
    left: 700px;
    top: 594px;
    width: 450px;
    margin: 0;
    text-align: center;
    color: var(--white);
    font-weight: 700;
    font-size: 50px;
    line-height: 56px;
    letter-spacing: -0.5px;
    text-shadow: 3px 3px 0 var(--leaf-deep);
  }
</style>
</head>
<body>
  <main class="card">
    <svg class="card-art" viewBox="0 0 1200 800" aria-hidden="false">
      <defs>
        <linearGradient id="photo-tone" x1="0" y1="0" x2="0" y2="1">
          <stop offset="0" stop-color="var(--sky-top)"/>
          <stop offset="0.35" stop-color="var(--sky-mid)"/>
          <stop offset="0.55" stop-color="#b9926f"/>
          <stop offset="0.75" stop-color="#4f7fa6"/>
          <stop offset="1" stop-color="#5f8a48"/>
        </linearGradient>
        <linearGradient id="green-fade" x1="0" y1="0" x2="0" y2="1">
          <stop offset="0" stop-color="var(--leaf)" stop-opacity="0"/>
          <stop offset="0.35" stop-color="var(--leaf)" stop-opacity="1"/>
          <stop offset="1" stop-color="var(--leaf)"/>
        </linearGradient>
        <clipPath id="photo-clip">
          <path d="M580 0 H1200 V800 H700 C640 700 520 640 480 520 C440 380 470 150 580 0 Z"/>
        </clipPath>
      </defs>

      <path class="arc-outer" d="M560 0 C450 150 420 380 462 520 C505 650 620 710 680 800"
            fill="none" stroke="var(--sky-line)" stroke-width="26"/>
      <path class="arc-inner" d="M575 0 C465 150 438 380 478 520 C520 650 630 710 694 800"
            fill="none" stroke="var(--ocean)" stroke-width="14"/>

      <g clip-path="url(#photo-clip)">
        <rect class="photo" x="440" y="0" width="760" height="800" fill="url(#photo-tone)"
              role="img" aria-label="Photo of six smiling friends hugging under palm trees on a sunny day"/>
        <rect class="offer-band" x="440" y="520" width="760" height="280" fill="url(#green-fade)"/>
      </g>

      <path class="wave-edge" d="M0 520 C140 440 380 410 520 500 C600 560 650 690 688 800 H0 Z"
            fill="var(--sky-line)"/>
      <path class="wave" d="M0 540 C140 462 370 436 505 520 C585 575 630 690 668 800 H0 Z"
            fill="var(--ocean)"/>
    </svg>

    <div class="brand">
      <div class="brand-mark"></div>
      <p class="brand-name">Sunny Circle</p>
    </div>

    <h1 class="headline">
      <span class="headline-top">SPREAD <small>THE</small></span>
      <span class="headline-main">SMILE..</span>
    </h1>

    <p class="offer">YOUR FRIEND<br>OR FAMILY<br>RECEIVES&nbsp; $ 25!!</p>
  </main>
</body>
</html>
```